custom carpentry, woodworking and home repair company needs logo design and business card design

Attention: I apologize but I just received notification from my state that I cannot use the company name that I originally submitted (Lumbrella). The new name will be Lumbrella We need a company logo and business card design for our new company based in the Hampton Roads area of Virginia. The company name is Lumbrella. The final design should give a first impression of true craftsmanship and attention to detail. We would like the card to include the company name, my name Derek Halloway (owner), phone number (757) 482-3175, website (lumbrella-shop.example) and email address (derek@lumbrella-shop.example). Everything else is up to your discretion. Thanks, have fun, and good luck.

Industry/Entity Type

Business

Contact Information for Business Card

See project description

Logo Text

see project description

Colors

Designer to choose colors to be used in the design.

```html
<!DOCTYPE html>
<html lang="en">
<head>
<meta charset="utf-8">
<title>Lumbrella – Business Card</title>
<link rel="stylesheet" href="https://fonts.googleapis.com/css2?family=Montserrat:wght@400;500;700&display=swap">
<style>
  :root {
    --page-bg: #ece9e4;
    --card-bg: #ffffff;
    --brand-blue: #2b3990;
    --brand-orange: #f08a24;
    --ink: #2e2e2e;
  }
  html, body {
    margin: 0;
    padding: 0;
    width: 1200px;
    height: 798px;
    overflow: hidden;
    background: var(--page-bg);
    font-family: "Montserrat", sans-serif;
  }
  .canvas {
    position: relative;
    width: 1200px;
    height: 798px;
  }
  .business-card {
    position: absolute;
    left: 180px;
    top: 159px;
    width: 840px;
    height: 480px;
    background: var(--card-bg);
    box-shadow: 0 10px 30px rgba(0,0,0,0.12);
  }
  .card-frame {
    position: absolute;
    inset: 24px;
    border: 2px solid var(--brand-blue);
  }
  .brand-block {
    position: absolute;
    left: 70px;
    top: 0;
    width: 330px;
    height: 480px;
    display: flex;
    flex-direction: column;
    align-items: center;
    justify-content: center;
    gap: 18px;
  }
  .brand-mark {
    width: 34px;
    height: 34px;
    background: var(--brand-blue);
  }
  .brand-name {
    font-weight: 700;
    font-size: 28px;
    letter-spacing: 1px;
    text-transform: uppercase;
    color: var(--brand-blue);
    white-space: nowrap;
  }
  .divider {
    position: absolute;
    left: 432px;
    top: 176px;
    width: 3px;
    height: 128px;
    background: var(--brand-orange);
  }
  .contact-block {
    position: absolute;
    left: 466px;
    top: 166px;
    color: var(--ink);
  }
  .person-name {
    margin: 0;
    font-weight: 700;
    font-size: 28px;
    letter-spacing: 0.8px;
    color: var(--brand-blue);
    text-transform: uppercase;
    white-space: nowrap;
  }
  .person-role {
    margin: 2px 0 20px;
    font-weight: 500;
    font-size: 17px;
    letter-spacing: 0.6px;
    text-transform: uppercase;
  }
  .contact-line {
    display: flex;
    align-items: center;
    gap: 12px;
    font-size: 17px;
    font-weight: 400;
    margin-bottom: 8px;
    white-space: nowrap;
  }
  .contact-icon {
    width: 16px;
    height: 16px;
    flex: none;
  }
</style>
</head>
<body>
<div class="canvas">
  <div class="business-card">
    <div class="card-frame"></div>

    <div class="brand-block">
      <div class="brand-mark"></div>
      <div class="brand-name">Lumbrella</div>
    </div>

    <div class="divider"></div>

    <div class="contact-block">
      <h1 class="person-name">Derek Halloway</h1>
      <p class="person-role">Owner</p>
      <div class="contact-line">
        <svg class="contact-icon" viewBox="0 0 16 16" aria-hidden="true">
          <rect x="4" y="1" width="8" height="14" rx="1.5" fill="none" stroke="#2b3990" stroke-width="1.5"/>
          <line x1="7" y1="12.5" x2="9" y2="12.5" stroke="#2b3990" stroke-width="1.2"/>
        </svg>
        <span class="contact-text">(757) 482-3175</span>
      </div>
      <div class="contact-line">
        <svg class="contact-icon" viewBox="0 0 16 16" aria-hidden="true">
          <rect x="1" y="3" width="14" height="10" fill="#2b3990"/>
          <polyline points="1,3 8,9 15,3" fill="none" stroke="#ffffff" stroke-width="1.2"/>
        </svg>
        <span class="contact-text">derek@lumbrella-shop.example</span>
      </div>
      <div class="contact-line">
        <svg class="contact-icon" viewBox="0 0 16 16" aria-hidden="true">
          <circle cx="8" cy="8" r="6.5" fill="none" stroke="#2b3990" stroke-width="1.4"/>
          <ellipse cx="8" cy="8" rx="2.8" ry="6.5" fill="none" stroke="#2b3990" stroke-width="1.2"/>
          <line x1="1.5" y1="8" x2="14.5" y2="8" stroke="#2b3990" stroke-width="1.2"/>
        </svg>
        <span class="contact-text">lumbrella-shop.example</span>
      </div>
    </div>
  </div>
</div>
</body>
</html>
```